Design Front Page Website for Nonprofit

Hello Freelancers!

I am looking for a creative designer that can create an illustrative front page design for a website landing page.

Company: Nonprofit that gives goods to charitable organization.

Primary Colors: #193D66, #7FD0F3

Looking for a creative/ultra modern design. Attached are examples (PDF) with directions on what I am looking for.

Need these designs done ASAP. Looking to award within 24 hrs. Launching site by Monday.

```html
<!DOCTYPE html>
<html lang="en">
<head>
<meta charset="utf-8">
<title>GiveCrate – Donate Goods. The Easy Way.</title>
<link rel="stylesheet" href="https://fonts.googleapis.com/css2?family=Inter:wght@400;500;600;700;800&display=swap">
<style>
  :root {
    --navy: #193D66;
    --sky: #7FD0F3;
    --ink: #1b1b1b;
    --text: #2a2a2a;
    --muted: #9a9a9a;
    --rule: #e6e6e6;
    --band: #f5f5f5;
    --badge: #2b2b2b;
    --white: #ffffff;
  }
  * { box-sizing: border-box; margin: 0; padding: 0; }
  html, body { width: 1200px; height: 859px; overflow: hidden; background: var(--white); }
  body { font-family: "Inter", Arial, sans-serif; color: var(--text); position: relative; }

  .site-header { position: absolute; top: 0; left: 0; width: 1200px; height: 72px; }
  .brand { position: absolute; left: 227px; top: 28px; font-size: 13px; font-weight: 700; color: var(--ink); }
  .main-nav { position: absolute; top: 29px; left: 0; font-size: 11px; font-weight: 600; color: var(--ink); }
  .main-nav a { position: absolute; white-space: nowrap; color: inherit; text-decoration: none; }
  .main-nav .caret { display: inline-block; margin-left: 6px; vertical-align: 1px; }
  .btn-donate { position: absolute; left: 926px; top: 22px; width: 96px; height: 28px; background: var(--sky); color: var(--white); font-size: 11px; font-weight: 600; border-radius: 3px; display: flex; align-items: center; justify-content: center; text-decoration: none; }

  .hero { position: absolute; top: 0; left: 0; width: 1200px; text-align: center; }
  .eyebrow { position: absolute; top: 103px; width: 1200px; font-size: 10.5px; font-weight: 700; color: var(--ink); }
  .headline { position: absolute; top: 128px; width: 1200px; font-size: 48px; line-height: 44px; font-weight: 800; letter-spacing: -1.5px; color: var(--ink); }
  .lede { position: absolute; top: 231px; width: 1200px; font-size: 16px; line-height: 22px; font-weight: 400; color: var(--text); }
  .btn-learn { position: absolute; left: 515px; top: 296px; width: 170px; height: 33px; background: var(--navy); color: var(--white); font-size: 11px; font-weight: 700; border-radius: 2px; display: flex; align-items: center; justify-content: center; text-decoration: none; }
  .fineprint { position: absolute; top: 336px; width: 1200px; font-size: 8.5px; color: var(--muted); }

  .compare { position: absolute; top: 0; left: 0; width: 1200px; }
  .compare h2 { position: absolute; top: 424px; font-size: 14px; font-weight: 700; color: var(--ink); text-align: center; }
  .compare .col-left { left: 250px; width: 250px; }
  .compare .col-right { left: 700px; width: 250px; }
  .divider { position: absolute; left: 600px; top: 424px; width: 1px; height: 218px; background: var(--rule); }
  .versus { position: absolute; left: 593px; top: 526px; font-size: 10px; color: var(--muted); }
  .art { position: absolute; border-radius: 8px; }
  .art-traditional { left: 302px; top: 452px; width: 160px; height: 210px; background: linear-gradient(160deg, #f4c9a6 0%, #e9a078 45%, #d9d2c6 100%); }
  .art-better-way { left: 648px; top: 468px; width: 356px; height: 176px; border-radius: 90px; background: linear-gradient(160deg, #e7eef0 0%, #b9dfd5 45%, #f0b49a 100%); }

  .partners { position: absolute; top: 703px; left: 0; width: 1200px; height: 105px; background: var(--band); }
  .partners-label { position: absolute; top: 31px; width: 1200px; text-align: center; font-size: 6.5px; letter-spacing: 0.6px; text-transform: uppercase; color: #b5b5b5; }
  .partner-row { position: absolute; top: 53px; left: 215px; width: 775px; height: 20px; display: flex; justify-content: space-between; align-items: center; }
  .partner-badge { height: 12px; background: var(--badge); border-radius: 2px; opacity: 0.85; }
</style>
</head>
<body>
  <header class="site-header">
    <div class="brand">Your Logo</div>
    <nav class="main-nav">
      <a style="left:386px">Our Story</a>
      <a style="left:465px">Our Work</a>
      <a style="left:548px">Our Team</a>
      <a style="left:631px">Get Involved<svg class="caret" width="7" height="5" viewBox="0 0 7 5"><path d="M1 1l2.5 2.5L6 1" fill="none" stroke="#1b1b1b" stroke-width="1.2"/></svg></a>
      <a style="left:729px">Contact us</a>
    </nav>
    <a class="btn-donate">Donate now</a>
  </header>

  <section class="hero">
    <p class="eyebrow">100% Online Donations Go Directly to Charity</p>
    <h1 class="headline">Donate Goods.<br>The Easy Way.</h1>
    <p class="lede">GiveCrate is the smarter, trustworthy, more efficient<br>way to donate goods to local charities.</p>
    <a class="btn-learn">Learn more!</a>
    <p class="fineprint">100% Online Donations Go Directly to Charity</p>
  </section>

  <section class="compare">
    <h2 class="col-left">Traditional Donations</h2>
    <h2 class="col-right">The GiveCrate Way</h2>
    <div class="divider"></div>
    <span class="versus">vs</span>
    <div class="art art-traditional" role="img" aria-label="Illustration of an elderly couple puzzled over a jar of coins, unsure how to donate"></div>
    <div class="art art-better-way" role="img" aria-label="Illustration of a busy town where people carry donated goods into a large crate with a red cross"></div>
  </section>

  <section class="partners">
    <p class="partners-label">Our partnerships</p>
    <div class="partner-row">
      <span class="partner-badge" style="width:52px"></span>
      <span class="partner-badge" style="width:50px"></span>
      <span class="partner-badge" style="width:34px"></span>
      <span class="partner-badge" style="width:56px"></span>
      <span class="partner-badge" style="width:48px"></span>
      <span class="partner-badge" style="width:44px"></span>
      <span class="partner-badge" style="width:54px"></span>
      <span class="partner-badge" style="width:56px"></span>
      <span class="partner-badge" style="width:56px"></span>
      <span class="partner-badge" style="width:50px"></span>
      <span class="partner-badge" style="width:56px"></span>
    </div>
  </section>
</body>
</html>
```